Veridan Support Coordination

My new business involves providing support coordination for QLPC participants that live with a primary psychosocial and/or developmental delay disability, including but not limited to:

- Anxiety
- Depression
- Bipolar
- Borderline Personality Disorder
- Schizophrenia
- Psychosis
- Autisim Spectrum Disorder
- Fetal Alcohol Spectrum Disorder
- Cerebral Palsy
- Intellectual Disability
- Acquired Brain Injury
- Down Syndrome
- Spina Bifida

The following is an example of another company
https://tallowmerebrook.com/

The are basically 3 types of support we offer
- psychosocial recovery coaching
- support coordination
- specialist support coordination

I have attached a copy of my logo, please utilise this colour scheme for website and business cards.

Target Market(s)

See above

Industry/Entity Type

Health Service

Number of Pages Required

5+ page

Font styles to use
Other font styles liked:
• Arial

Colors

Designer to choose only greyscale colors for use in the design.

```html
<!DOCTYPE html>
<html lang="en">
<head>
<meta charset="utf-8">
<title>Veridan Support Coordination</title>
<link href="https://fonts.googleapis.com/css2?family=Mulish:ital,wght@0,400;0,600;0,700;0,800;0,900;1,400&family=Montserrat:wght@700&display=swap" rel="stylesheet">
<style>
:root{
  --blue:#1a8fd8;
  --blue-dark:#1273b8;
  --green:#84c225;
  --green-soft:#a7d45c;
  --page:#f3f7ec;
  --ink:#222;
  --muted:#6b6b6b;
  --white:#fff;
  --black:#000;
  --social-1:#3b5a9a;
  --social-2:#1da1f2;
  --social-3:#e3262c;
  --social-4:#b53c9a;
}
*{margin:0;padding:0;box-sizing:border-box}
html,body{width:1200px;height:3467px;overflow:hidden}
body{position:relative;background:var(--page);font-family:'Mulish',Arial,sans-serif;color:var(--ink)}
.abs{position:absolute}

/* header */
.site-header{position:absolute;left:0;top:0;width:1200px;height:151px;background:#f7f9f3;border-top:3px solid var(--blue)}
.brand{position:absolute;left:110px;top:30px;display:flex;align-items:center;gap:12px}
.brand-dot{width:40px;height:40px;border-radius:50%;background:var(--green)}
.brand-text{display:flex;flex-direction:column;line-height:1}
.brand-name{font-size:40px;font-weight:400;color:var(--blue);letter-spacing:-0.5px}
.brand-sub{font-size:12px;font-weight:400;color:var(--blue);margin-top:3px;padding-left:10px}
.call{position:absolute;left:650px;top:22px}
.call-label{position:absolute;left:54px;top:0;font-size:13px;color:#333;white-space:nowrap}
.call-number{position:absolute;left:54px;top:16px;font-size:21px;font-weight:700;color:#222;white-space:nowrap}
.social{position:absolute;top:20px;width:38px;height:38px;border-radius:50%;display:flex;align-items:center;justify-content:center}
.nav{position:absolute;top:99px;font-size:17px;color:#222}
.nav.active{color:var(--blue)}
.btn{position:absolute;display:flex;align-items:center;justify-content:center;color:var(--white);font-weight:700;border-radius:26px;font-size:14px;text-transform:uppercase}
.btn-quote{left:897px;top:86px;width:191px;height:50px;background:var(--blue);font-size:15px}

/* hero */
.hero{position:absolute;left:0;top:151px;width:1200px;height:640px;background:linear-gradient(90deg,#5fbf4a 0%,#5cb97a 22%,#8fb8b0 45%,#c9c9c0 70%,#a7997e 100%)}
.hero-shade{position:absolute;inset:0;background:linear-gradient(180deg,rgba(140,200,80,.35),rgba(30,150,140,.55))}
.hero-title{position:absolute;left:111px;top:302px;font-family:'Montserrat',Arial,sans-serif;font-size:62px;font-weight:700;color:var(--white)}
.hero-text{position:absolute;left:112px;top:381px;width:520px;font-size:15px;line-height:25px;color:var(--white)}
.btn-start{left:113px;top:444px;width:157px;height:51px;background:var(--blue)}
.hero-curve{position:absolute;left:0;top:700px}

/* services */
.service{position:absolute;top:639px;width:312px;text-align:center}
.service-photo{height:229px;border:4px solid var(--white);border-radius:4px;box-shadow:0 6px 14px rgba(0,0,0,.18)}
.service-icon{position:absolute;left:112px;top:157px;width:88px;height:88px;border-radius:50%;background:var(--white);border:4px solid var(--green-soft);display:flex;align-items:center;justify-content:center}
.service-title{margin-top:30px;font-size:23px;line-height:26px;color:#222;font-weight:600}
.service-text{margin-top:16px;font-size:15px;line-height:26px;color:var(--muted)}

/* about */
.about-ring{position:absolute;left:128px;top:1083px}
.section-title{position:absolute;font-size:36px;font-weight:900;text-transform:uppercase;letter-spacing:-0.5px}
.underline{position:absolute;height:3px;background:var(--blue)}
.about-text{position:absolute;left:600px;top:1164px;width:480px;font-size:14px;line-height:25.7px;color:#555}
.btn-learn{left:600px;top:1440px;width:157px;height:49px;background:var(--green)}

/* why */
.why-panel{position:absolute;left:0;top:1583px;width:600px;height:535px;background:var(--green)}
.why-photo{position:absolute;left:600px;top:1583px;width:600px;height:535px;background:linear-gradient(135deg,#d8dde0,#9aa7b3 55%,#e8ecef)}
.why-title{position:absolute;left:110px;top:1648px;font-size:37px;font-weight:900;color:var(--white)}
.why-line{position:absolute;left:110px;top:1701px;width:80px;height:3px;background:var(--white)}
.why-intro{position:absolute;left:110px;top:1726px;width:440px;font-size:14px;line-height:25px;color:var(--white)}
.feature{position:absolute;width:220px;color:var(--white)}
.feature-icon{position:absolute;left:0;top:0;width:56px;height:56px;border-radius:50%;border:2px solid rgba(255,255,255,.85)}
.feature-icon::after{content:"";position:absolute;left:10px;top:10px;width:32px;height:32px;border-radius:50%;border:2px solid rgba(255,255,255,.8)}
.feature-name{position:absolute;left:66px;top:4px;font-size:19px;line-height:21px;text-transform:uppercase;white-space:nowrap}
.feature-text{position:absolute;left:0;top:77px;width:220px;font-size:13.5px;line-height:21px}

/* conditions */
.condition{position:absolute;top:2128px;width:225px;height:313px;border-radius:4px}
.condition-label{position:absolute;left:0;right:0;bottom:28px;text-align:center;color:var(--white);font-size:21px;font-weight:700}
.condition-label.center{bottom:auto;top:140px}
.carousel-arrow{position:absolute;top:2260px;width:48px;height:48px;border-radius:50%;background:var(--green)}

/* testimonials */
.quote{position:absolute;left:190px;top:2606px;width:820px;text-align:center;font-size:14.5px;line-height:25.7px;font-style:italic;color:#666}
.avatar{position:absolute;border-radius:50%}

/* footer */
.footer-shape{position:absolute;left:0;top:2880px}
.footer-brand{position:absolute;left:0;width:1200px;top:2952px;text-align:center;color:var(--white)}
.footer-brand .brand-dot{display:inline-block;width:78px;height:78px;border:3px solid var(--white);background:transparent}
.footer-name{display:block;font-size:52px;font-weight:400;line-height:56px;margin-top:4px}
.footer-sub{display:block;font-size:17px;line-height:18px;padding-left:20px}
.footer-rule{position:absolute;left:110px;width:978px;height:1px;background:#3a3a3a}
.footer-col{position:absolute;top:3150px;color:var(--white)}
.footer-col h3{font-size:22px;font-weight:600;margin-bottom:20px}
.footer-col li{list-style:none;font-size:15px;line-height:25.7px}
.footer-col li::before{content:"» ";}
.contact-row{display:flex;gap:14px;font-size:15px;line-height:25.7px;margin-bottom:25px}
.contact-row svg{flex:none;margin-top:5px}
.copyright{position:absolute;left:0;width:1200px;top:3397px;text-align:center;color:var(--white);font-size:14px}
</style>
</head>
<body>

<header class="site-header">
  <div class="brand"><span class="brand-dot"></span><span class="brand-text"><span class="brand-name">Veridan</span><span class="brand-sub">support coordination</span></span></div>
  <div class="call">
    <svg width="42" height="42" viewBox="0 0 42 42" fill="none" stroke="#8ccf3a" stroke-width="2.2"><path d="M10 6l6 7-4 4c2 5 6 9 11 11l4-4 7 6-4 5C18 34 6 22 5 10z"/><path d="M24 10a8 8 0 0 1 8 8M24 4a14 14 0 0 1 14 14"/></svg>
    <span class="call-label">Call us :</span>
    <span class="call-number">+1 555 014 2276</span>
  </div>
  <span class="social" style="left:910px;background:var(--social-1)" aria-label="Social profile">
    <svg width="18" height="18" viewBox="0 0 18 18" fill="none" stroke="#fff" stroke-width="1.8"><path d="M3 4h12v8H8l-4 3v-3H3z"/></svg>
  </span>
  <span class="social" style="left:955px;background:var(--social-2)" aria-label="Social profile">
    <svg width="18" height="18" viewBox="0 0 18 18" fill="none" stroke="#fff" stroke-width="1.8"><path d="M7.5 10.5l3-3M6 8L4 10a2.5 2.5 0 0 0 4 4l2-2M12 10l2-2a2.5 2.5 0 0 0-4-4L8 6"/></svg>
  </span>
  <span class="social" style="left:999px;background:var(--social-3)" aria-label="Social profile">
    <svg width="18" height="18" viewBox="0 0 18 18" fill="none" stroke="#fff" stroke-width="1.8"><circle cx="5" cy="9" r="2"/><circle cx="13" cy="4.5" r="2"/><circle cx="13" cy="13.5" r="2"/><path d="M7 8l4-2.5M7 10l4 2.5"/></svg>
  </span>
  <span class="social" style="left:1043px;background:var(--social-4)" aria-label="Social profile">
    <svg width="18" height="18" viewBox="0 0 18 18" fill="none" stroke="#fff" stroke-width="1.8"><path d="M9 2l2 4.5 5 .5-3.7 3.3 1 4.7L9 12.6 4.7 15l1-4.7L2 7l5-.5z"/></svg>
  </span>
  <span class="nav active" style="left:378px">Home</span>
  <span class="nav" style="left:471px">About us</span>
  <span class="nav" style="left:590px">Services</span>
  <span class="nav" style="left:702px">Blog</span>
  <span class="nav" style="left:784px">Contact us</span>
  <span class="btn btn-quote">Request a quote</span>
</header>

<section class="hero" role="img" aria-label="Photo of smiling colleagues meeting in an office, one in a wheelchair, under a green to teal tint">
  <div class="hero-shade"></div>
</section>
<div class="hero-title">Veridan</div>
<p class="hero-text">Lorem ipsum dolor sit amet, consectetur adipiscing elit, sed do eiusmod tempor incididunt ut labore et dolore magna aliqua. Ut enim</p>
<span class="btn btn-start">Get started</span>
<svg class="hero-curve" width="1200" height="160" viewBox="0 0 1200 160"><path d="M0 27 Q600 130 1200 47 L1200 160 L0 160 Z" fill="var(--page)"/></svg>

<div class="service" style="left:112px">
  <div class="service-photo" role="img" aria-label="Photo of a parent helping a child with schoolwork" style="background:linear-gradient(135deg,#c9b9a3,#e6ddd0 60%,#a8b7c7)"></div>
  <div class="service-icon"><svg width="46" height="46" viewBox="0 0 46 46" fill="none" stroke="#333" stroke-width="1.8"><circle cx="23" cy="23" r="14"/><circle cx="23" cy="22" r="5"/></svg></div>
  <h3 class="service-title">Psychosocial<br>recovery coaching</h3>
  <p class="service-text">Lorem ipsum dolor sit amet, adipiscing<br>consectetur gravida elit</p>
</div>
<div class="service" style="left:445px">
  <div class="service-photo" role="img" aria-label="Photo of joined hands holding a small green seedling" style="background:linear-gradient(135deg,#8a6a4e,#b59170 50%,#5d4634)"></div>
  <div class="service-icon"><svg width="46" height="46" viewBox="0 0 46 46" fill="none" stroke="#333" stroke-width="1.8"><circle cx="23" cy="14" r="4"/><circle cx="12" cy="30" r="4"/><circle cx="34" cy="30" r="4"/><path d="M23 20v6M16 30h14"/></svg></div>
  <h3 class="service-title">Support<br>coordination</h3>
  <p class="service-text">Lorem ipsum dolor sit amet, adipiscing<br>consectetur gravida elit</p>
</div>
<div class="service" style="left:777px">
  <div class="service-photo" role="img" aria-label="Photo of a business team meeting around a desk" style="background:linear-gradient(135deg,#e9ecef,#b7bcc2 55%,#f1f1f1)"></div>
  <div class="service-icon"><svg width="46" height="46" viewBox="0 0 46 46" fill="none" stroke="#333" stroke-width="1.8"><rect x="10" y="10" width="11" height="11"/><rect x="25" y="10" width="11" height="11"/><rect x="10" y="25" width="11" height="11"/><path d="M28 28l6 6M34 28l-6 6"/></svg></div>
  <h3 class="service-title">Specialist<br>support coordination</h3>
  <p class="service-text">Lorem ipsum dolor sit amet, adipiscing<br>consectetur gravida elit</p>
</div>

<svg class="about-ring" width="430" height="430" viewBox="0 0 430 430">
  <defs><linearGradient id="aboutFill" x1="0" y1="0" x2="1" y2="1"><stop offset="0" stop-color="#d6ebf5"/><stop offset=".55" stop-color="#a9d2ea"/><stop offset="1" stop-color="#3f5f48"/></linearGradient></defs>
  <circle cx="215" cy="215" r="210" fill="none" stroke="#4c6a52" stroke-width="4"/>
  <circle cx="215" cy="215" r="200" fill="none" stroke="#9fb8a4" stroke-width="2"/>
  <circle cx="215" cy="215" r="150" fill="url(#aboutFill)" role="img" aria-label="Illustration of hands holding paperwork"/>
</svg>
<h2 class="section-title" style="left:600px;top:1096px"><span style="color:var(--blue)">About</span> <span style="color:var(--green)">Veridan</span></h2>
<div class="underline" style="left:600px;top:1149px;width:80px"></div>
<p class="about-text">Lorem ipsum dolor sit amet, consectetur adipiscing elit, sed do eiusmod tempor incididunt ut labore et dolore magna aliqua. Ut enim ad minim veniam, quis nostrud exercitation ullamco laboris nisi ut aliquip ex ea commodo consequat. Duis aute irure dolor in reprehenderit in voluptate velit esse cillum dolore eu fugiat nulla pariatur. Excepteur sint occaecat cupidatat non proident, sunt in culpa qui officia deserunt mollit anim id est laborum. Lorem ipsum dolor sit amet, consectetur adipiscing elit, sed do eiusmod tempor incididunt ut labore et dolore magna aliqua. Ut enim ad minim veniam, quis nostrud exercitation ullamco laboris nisi ut aliquip ex ea commodo</p>
<span class="btn btn-learn">Learn more ➜</span>

<section class="why-panel"></section>
<div class="why-photo" role="img" aria-label="Photo of a couple reviewing documents together at a table"></div>
<h2 class="why-title">WHY CHOOSE US</h2>
<div class="why-line"></div>
<p class="why-intro">Lorem ipsum dolor sit amet, consectetur adipiscing elit, sed do eiusmod tempor incididunt ut labore et dolore magna aliqua.</p>
<div class="feature" style="left:110px;top:1794px"><span class="feature-icon"></span><span class="feature-name">25 years of<br>experience</span><p class="feature-text">Lorem ipsum dolor sit amet, consectetur adipiscing elit</p></div>
<div class="feature" style="left:344px;top:1794px"><span class="feature-icon"></span><span class="feature-name">24/7<br>support</span><p class="feature-text">Lorem ipsum dolor sit amet, consectetur adipiscing elit</p></div>
<div class="feature" style="left:110px;top:1948px"><span class="feature-icon"></span><span class="feature-name">No policy<br>fees</span><p class="feature-text">Lorem ipsum dolor sit amet, consectetur adipiscing elit</p></div>
<div class="feature" style="left:344px;top:1948px"><span class="feature-icon"></span><span class="feature-name">Growing<br>your business</span><p class="feature-text">Lorem ipsum dolor sit amet, consectetur adipiscing elit</p></div>

<div class="condition" style="left:8px;background:linear-gradient(180deg,#8f939a,#3d4148)" role="img" aria-label="Photo of a distressed woman"><span class="condition-label">Anxiety</span></div>
<div class="condition" style="left:249px;background:linear-gradient(180deg,#9aa29a,#2c2f33)" role="img" aria-label="Photo of a worried man"><span class="condition-label">Depression</span></div>
<div class="condition" style="left:487px;background:linear-gradient(180deg,#7cc44a,#2fa3c8 55%,#1e9ad9)" role="img" aria-label="Photo of a person holding a mask, with green and blue overlay"><span class="condition-label center">Bipolar</span></div>
<div class="condition" style="left:728px;background:linear-gradient(180deg,#bfc2c4,#3b3d40)" role="img" aria-label="Photo of a woman sitting with head in hands"><span class="condition-label">Schizophrenia</span></div>
<div class="condition" style="left:967px;background:linear-gradient(180deg,#d9d9d9,#6f6a66)" role="img" aria-label="Photo of a woman with a screaming double image"><span class="condition-label">Psychosis</span></div>
<svg class="carousel-arrow" style="left:0" viewBox="0 0 48 48"><path d="M27 17l-7 7 7 7" fill="none" stroke="#fff" stroke-width="2.5"/></svg>
<svg class="carousel-arrow" style="left:1148px" viewBox="0 0 48 48"><path d="M21 17l7 7-7 7" fill="none" stroke="#fff" stroke-width="2.5"/></svg>

<h2 class="section-title" style="left:0;width:1200px;text-align:center;top:2526px"><span style="color:var(--blue)">What</span> <span style="color:var(--green)">client</span> <span style="color:var(--blue)">says</span></h2>
<div class="underline" style="left:560px;top:2579px;width:80px"></div>
<p class="quote">“Lorem ipsum dolor sit amet, consectetur adipiscing elit, sed do eiusmod tempor incididunt ut labore et dolore magna aliqua. Ut enim ad minim veniam, quis nostrud exercitation ullamco laboris nisi ut aliquip ex ea commodo consequat. Duis aute irure dolor in reprehenderit in voluptate velit esse cillum dolore eu fugiat nulla pariatur. Excepteur sint occaecat cupidatat non proident, sunt in culpa anim id est laborum”</p>
<svg class="abs" style="left:86px;top:2648px" width="14" height="20" viewBox="0 0 14 20"><path d="M10 3L3 10l7 7" fill="none" stroke="#222" stroke-width="2"/></svg>
<svg class="abs" style="left:1098px;top:2648px" width="14" height="20" viewBox="0 0 14 20"><path d="M4 3l7 7-7 7" fill="none" stroke="#222" stroke-width="2"/></svg>
<div class="avatar" style="left:362px;top:2734px;width:72px;height:72px;background:#b7b3ae" role="img" aria-label="Client portrait"></div>
<div class="avatar" style="left:463px;top:2734px;width:72px;height:72px;background:#9fb3c6" role="img" aria-label="Client portrait"></div>
<div class="avatar" style="left:552px;top:2722px;width:96px;height:96px;background:#a9b9c8;border:4px solid var(--blue);box-shadow:0 0 0 4px var(--white) inset" role="img" aria-label="Client portrait, selected"></div>
<div class="avatar" style="left:665px;top:2734px;width:72px;height:72px;background:#a8a29b" role="img" aria-label="Client portrait"></div>
<div class="avatar" style="left:764px;top:2734px;width:72px;height:72px;background:#8fa4bc" role="img" aria-label="Client portrait"></div>

<svg class="footer-shape" width="1200" height="587" viewBox="0 0 1200 587">
  <path d="M120 122 Q600 -20 1080 110" fill="none" stroke="var(--green)" stroke-width="6"/>
  <path d="M0 126 Q600 -30 1200 126 L1200 587 L0 587 Z" fill="var(--black)"/>
</svg>
<div class="footer-brand"><span class="brand-dot"></span><span class="footer-name">Veridan</span><span class="footer-sub">support coordination</span></div>
<div class="footer-rule" style="top:3123px"></div>
<div class="footer-col" style="left:183px"><h3>Quick Links</h3><ul><li>Home</li><li>About us</li><li>Services</li><li>Blog</li><li>Contact us</li></ul></div>
<div class="footer-col" style="left:457px"><h3>Our Services</h3><ul><li>Anxiety</li><li>Depression</li><li>Bipolar</li><li>Borderline Personality Disorder</li><li>Schizophrenia</li><li>More</li></ul></div>
<div class="footer-col" style="left:777px"><h3>Contact us</h3>
  <div class="contact-row"><svg width="14" height="16" viewBox="0 0 14 16"><path d="M7 1a5 5 0 0 0-5 5c0 4 5 9 5 9s5-5 5-9a5 5 0 0 0-5-5z" fill="#fff"/><circle cx="7" cy="6" r="2" fill="#000"/></svg><span>Lorem ipsum dolor sit amet,<br>consectetur elit</span></div>
  <div class="contact-row"><svg width="14" height="14" viewBox="0 0 14 14"><path d="M3 1l3 3-2 2c1 2 2 3 4 4l2-2 3 3-2 2C5 13 1 9 1 3z" fill="#fff"/></svg><span>+1 555 014 2276</span></div>
  <div class="contact-row"><svg width="14" height="12" viewBox="0 0 14 12"><rect x="0.5" y="1" width="13" height="10" fill="#fff"/><path d="M1 2l6 5 6-5" fill="none" stroke="#000" stroke-width="1.2"/></svg><span>hello@veridansupport.com</span></div>
</div>
<div class="footer-rule" style="top:3379px"></div>
<p class="copyright">© 2020 Veridan Support Coordination. All rights reserved.</p>

</body>
</html>
```